Business Card Design

New business, starting out small. High end residential/ commercial building company in Sydney Australia's prestigious Eastern suburbs, perfection is our motto and we want our marketing design to reflect that.

Therefore marketing towards high end clients. Looking for design concepts that will portray this image and will appeal to both male and females, prototype has been included- see images. Although we are open to ideas we have included this to give direction.

DARK Navy and white is the colour scheme, as per image provided. Logo ideas welcomed, however design is preferred simple, modern and sophisticated.

This business card will be the template and inspiration for website, t-shirt, banners etc to come so if you want the business, show us your design!

Industry/Entity Type

Marketing

Contact Information for Business Card

Company name: Harbourline Craft Building
Catch phrase: Your vision
Owner/operator: Trevor Ashcombe
Phone: 0498152604
Website: www.harbourlinecraftbuilding.com.au
Licence No 518920K
ABN 72 915 804
Email address
(displayed on back of card):info@harbourlinecraftbuilding.com.au

```html
<!DOCTYPE html>
<html lang="en">
<head>
<meta charset="utf-8">
<title>Harbourline Craft Building — Business Card</title>
<link rel="stylesheet" href="https://fonts.googleapis.com/css2?family=Didact+Gothic&family=Montserrat:wght@600;700&display=swap">
<style>
  :root {
    --navy: #221e5f;
    --white: #ffffff;
    --paper: #fbfbfd;
    --rule: #9a9aa3;
    --grey-text: #6f6f78;
    --backdrop: #d9d9dc;
  }
  * { box-sizing: border-box; margin: 0; padding: 0; }
  html, body {
    width: 1200px; height: 830px; overflow: hidden;
    background: var(--backdrop);
    font-family: "Didact Gothic", "Century Gothic", sans-serif;
  }
  .stage { position: relative; width: 1200px; height: 830px; }
  .card {
    position: absolute; left: 290px; width: 620px; height: 354px;
    overflow: hidden; box-shadow: 0 6px 18px rgba(0,0,0,.18);
  }

  /* Back of card */
  .card--back { top: 44px; background: var(--navy); color: var(--white); }
  .card--back .texture {
    position: absolute; left: 0; right: 0; bottom: 0; height: 150px;
    background: linear-gradient(160deg, rgba(255,255,255,0) 30%, rgba(255,255,255,.06) 60%, rgba(255,255,255,.02) 100%);
  }
  .brand-mark {
    position: absolute; left: 0; right: 0; top: 72px;
    display: flex; align-items: center; justify-content: center; gap: 12px;
  }
  .brand-mark .dot { width: 22px; height: 22px; border-radius: 50%; flex: none; }
  .brand-mark .label {
    font-family: "Montserrat", sans-serif; font-weight: 700;
    font-size: 17px; letter-spacing: 1px; text-transform: uppercase;
  }
  .card--back .brand-mark .dot { background: var(--white); }
  .card--back .company {
    position: absolute; left: 0; right: 0; top: 158px; text-align: center;
    font-family: "Montserrat", sans-serif; font-weight: 700;
    font-size: 29px; letter-spacing: .5px; text-transform: uppercase;
  }
  .card--back .email {
    position: absolute; left: 0; right: 0; top: 202px; text-align: center;
    font-size: 17px; letter-spacing: .3px;
  }

  /* Front of card */
  .card--front { top: 432px; background: var(--paper); color: var(--navy); }
  .band-top {
    position: absolute; left: 0; top: 0; width: 100%; height: 56px;
    background: var(--navy); color: var(--white);
    display: flex; align-items: center; justify-content: center;
    font-family: "Montserrat", sans-serif; font-weight: 700;
    font-size: 26px; letter-spacing: .5px; text-transform: uppercase;
    border-bottom: 4px solid var(--rule);
  }
  .band-bottom {
    position: absolute; left: 0; bottom: 0; width: 100%; height: 64px;
    background: var(--navy); color: var(--white);
    display: flex; align-items: center; padding-left: 28px;
  }
  .band-bottom .web { font-size: 17px; letter-spacing: .3px; }
  .card--front .brand-mark {
    top: 122px; left: 20px; right: auto; width: 250px; flex-direction: column; gap: 10px;
  }
  .card--front .brand-mark .dot { background: var(--navy); width: 26px; height: 26px; }
  .card--front .brand-mark .label { font-size: 15px; text-align: center; color: var(--navy); }
  .divider {
    position: absolute; left: 290px; top: 74px; width: 3px; height: 196px; background: var(--rule);
  }
  .details {
    position: absolute; left: 300px; top: 56px; width: 320px; height: 234px;
    background: var(--white); padding: 26px 0 0 38px;
  }
  .details .name {
    font-family: "Montserrat", sans-serif; font-weight: 700;
    font-size: 20px; letter-spacing: .5px; text-transform: uppercase;
  }
  .details .role { color: var(--grey-text); font-size: 15px; margin-top: 2px; }
  .contact { margin-top: 18px; font-size: 16px; border-collapse: collapse; }
  .contact th { color: var(--grey-text); font-weight: 400; text-align: left; padding: 1px 10px 1px 0; }
  .contact td { padding: 1px 0; }
</style>
</head>
<body>
<main class="stage">

  <section class="card card--back" aria-label="Back of business card">
    <div class="texture" role="img" aria-label="Faint roofline pattern across the lower card"></div>
    <div class="brand-mark">
      <span class="dot"></span>
      <span class="label">Harbourline Craft Building</span>
    </div>
    <h1 class="company">Harbourline Craft Building</h1>
    <p class="email">info@harbourlinecraftbuilding.com.au</p>
  </section>

  <section class="card card--front" aria-label="Front of business card">
    <header class="band-top">Harbourline Craft Building</header>
    <div class="brand-mark">
      <span class="dot"></span>
      <span class="label">Harbourline Craft Building</span>
    </div>
    <div class="divider"></div>
    <div class="details">
      <p class="name">Trevor Ashcombe</p>
      <p class="role">Director</p>
      <table class="contact">
        <tr><th>Phone :</th><td>0498152604</td></tr>
        <tr><th>No&nbsp;&nbsp;&nbsp;&nbsp;&nbsp;&nbsp;&nbsp;:</th><td>518920K</td></tr>
        <tr><th>ABN&nbsp;&nbsp;&nbsp;&nbsp;:</th><td>72 915 804</td></tr>
      </table>
    </div>
    <footer class="band-bottom">
      <span class="web">www.harbourlinecraftbuilding.com.au</span>
    </footer>
  </section>

</main>
</body>
</html>
```